Texas Marsh Reed Conservation League

We need to design the home page of this new website. We would like a fun website design for provides as a resource for members and information for potential members.
Please design so that we can see a portion of background on each side on the website.
I just need the final design files psd no coding needed.
Attached is their logo (colors are not 100% set in stone either so can mess with those as I did in the quick mockup attached)
Attached is a pdf newsletter they send out, you can get a feel for them and what they are about. The design is crappy and we are here to fix that going forward and we are starting with the website.
Here are some quick example websites (design style is open)
- I attached a quick mockup i did just for a content visual but by all means do what you want.
- http://www.lonestarbizladies.org/
- http://www.wqrtf.org/
- http://demo.webkitpalette.com/demo.php?cat=html5themes&host=layoutbazaar&temp=veltrona
- http://www.fieldkeep.org/
- http://www.urbanpantry.org/
- http://www.projectcozy.org/
here are some of the other chapters website (pretty bad!)
and here are some of the others:
- http://www.kdwrcl.org/
- http://wrcl.org/
- http://www.gwrcl.org/
Content Items that need to be included:
1. Logo
2. Menu - home, about, members, resources, events, membership, contact
3. Become a member - button or action
4. social links - facebook, linkedin, youtube
5. banner - that needs to explain their purpose "Promoting environmental stewardship through operations, research, education and outreach" (or this can be worked into the design)
6. Upcoming event (s)
7. Advertisement - members can place an ad on the website, this can be a placeholder for now
8. newsletter signup
9. advertise with us - this link can be in the footer
30-60 years of age, succesfull (household budgets of 120K+ men and women that live in texas.
Education

```html
<!DOCTYPE html>
<html lang="en">
<head>
<meta charset="utf-8">
<title>Texas Marsh Reed Conservation League</title>
<link href="https://fonts.googleapis.com/css2?family=Didact+Gothic&family=Open+Sans:wght@400&family=Raleway:wght@500&family=Source+Sans+3:ital,wght@0,400;0,600;1,400&display=swap" rel="stylesheet">
<style>
:root{
  --navy:#0b2160;
  --navy-deep:#081a4f;
  --crimson:#9b2445;
  --crimson-text:#9a2a4a;
  --page:#f6f6f6;
  --ink:#1e1e1e;
  --muted:#333;
  --charcoal:#2c2c2c;
  --white:#fff;
}
*{margin:0;padding:0;box-sizing:border-box}
html,body{width:997px;height:1200px;overflow:hidden}
body{background:var(--page);font-family:"Source Sans 3",sans-serif;color:var(--ink);position:relative}
.abs{position:absolute}
.topbar{left:0;top:0;width:997px;height:37px;background:var(--navy)}
.social{display:flex;gap:10px}
.social span{display:block;width:21px;height:21px;border-radius:50%;background:var(--white)}
.topbar .social{position:absolute;left:638px;top:7px}
.toplinks{position:absolute;left:757px;top:11px;display:flex;gap:22px;font-family:"Didact Gothic",sans-serif;font-size:11.5px;color:var(--white)}
.toplinks a{color:inherit;text-decoration:none;display:flex;align-items:center;gap:5px}
.header{left:0;top:37px;width:997px;height:110px;background:#fafafa}
.logo-box{left:83px;top:0;width:243px;height:137px;background:var(--white);clip-path:polygon(0 0,100% 0,100% 80%,60% 80%,40% 100%,0 70%);display:flex;align-items:center;justify-content:center;gap:8px;padding-bottom:30px}
.logo-box i{display:block;width:22px;height:22px;background:var(--crimson);border-radius:50%}
.logo-box b{font-family:"Didact Gothic",sans-serif;font-weight:400;font-size:38px;color:var(--navy);letter-spacing:1px}
.site-title{left:376px;top:56px;font-family:"Didact Gothic",sans-serif;font-weight:400;font-size:23px;line-height:33px;color:#111;letter-spacing:.5px}
.site-title span{display:block}
.site-title span+span{padding-left:42px}
.join{left:734px;top:68px;width:179px;height:38px;background:#111;border:2px solid #111;outline:1px solid var(--white);outline-offset:-4px;border-radius:4px;color:var(--white);font-family:"Didact Gothic",sans-serif;font-size:15.5px;display:flex;align-items:center;justify-content:center}
.nav{left:0;top:147px;width:997px;height:41px;background:var(--crimson)}
.nav ul{list-style:none;font-family:"Source Sans 3",sans-serif;font-weight:600;font-size:14px;color:var(--white)}
.nav li{position:absolute;top:8px;height:25px;display:flex;align-items:center}
.nav li.active{background:var(--navy);border-radius:3px;width:70px;justify-content:center}
.events-title{left:85px;top:743px}
.slider{left:83px;top:198px;width:832px;height:351px;background:var(--white);border:1px solid #e2e2e2}
.slide{position:absolute;left:3px;top:3px;width:824px;height:344px;background:linear-gradient(180deg,#b9d3ee 0%,#dbe7f2 30%,#5f8a3a 45%,#3f5a2c 58%,#5a6a52 75%,#4a5f3a 100%)}
.arrow{position:absolute;top:132px;width:21px;height:27px;background:rgba(200,200,200,.85);display:flex;align-items:center;justify-content:center}
.caption{position:absolute;left:0;bottom:0;width:824px;height:78px;background:rgba(34,34,34,.82);color:var(--white);font-family:"Raleway",sans-serif;font-weight:500;font-size:21.5px;line-height:28px;padding:11px 18px;letter-spacing:.9px}
h2{font-family:"Didact Gothic",sans-serif;font-weight:400;font-size:27px;color:var(--crimson-text);letter-spacing:1px}
.welcome{left:86px;top:572px}
.intro{left:88px;top:612px;width:560px;font-family:"Open Sans",sans-serif;font-size:13px;line-height:18.3px;color:var(--muted)}
.newsletter{left:671px;top:578px;width:242px;height:140px;background:var(--navy);border-radius:3px;color:var(--white)}
.newsletter h3{font-family:"Didact Gothic",sans-serif;font-weight:400;font-size:22px;text-align:center;margin-top:12px;letter-spacing:.5px}
.newsletter .field{position:absolute;left:25px;top:52px;width:189px;height:27px;background:var(--white);color:#555;font-family:Arial,sans-serif;font-size:11.5px;padding:6px 6px}
.newsletter .btn{position:absolute;left:126px;top:94px;width:89px;height:28px;background:var(--crimson);border:1px solid #c04a6a;font-weight:600;font-size:15px;display:flex;align-items:center;justify-content:center;letter-spacing:.5px}
.event{left:86px;width:555px;height:86px}
.event .thumb{position:absolute;left:0;top:0;width:129px;height:86px}
.event .body{position:absolute;left:140px;top:0;width:415px}
.event h4{font-weight:600;font-size:12.5px;color:var(--navy)}
.event time{display:block;font-style:italic;font-size:12px;color:var(--crimson-text);margin-top:4px}
.event p{font-family:"Open Sans",sans-serif;width:390px;font-size:12px;line-height:16px;color:var(--muted);margin-top:3px;padding-left:1px}
.divider{left:83px;top:901px;width:557px;height:1px;background:#d9d9d9}
.viewall{left:533px;top:1033px;width:103px;height:27px;background:var(--charcoal);border-radius:4px;color:var(--white);font-family:"Didact Gothic",sans-serif;font-size:14px;display:flex;align-items:center;justify-content:center;letter-spacing:.5px}
.ad{left:672px;top:749px;width:242px;height:313px;background:linear-gradient(180deg,#4a8dbf 0%,#2a5a86 35%,#1e2a3a 60%,#222 78%,#e8e8e8 79%,#e0e0e0 100%)}
.footer{left:0;top:1106px;width:997px;height:94px;background:var(--navy-deep);color:var(--white);font-family:Arial,sans-serif}
.footnav{position:absolute;left:96px;top:23px;font-size:12px;display:flex}
.footnav span.sep{margin:0 18px}
.copy{position:absolute;left:96px;top:53px;font-size:12px}
.advertise{position:absolute;left:781px;top:19px;font-size:13.5px;text-decoration:underline;color:var(--white)}
.footer .social{position:absolute;left:802px;top:50px;gap:12px}
</style>
</head>
<body>
<header>
  <div class="abs topbar">
    <div class="social" aria-label="Social profile links"><span aria-label="Social profile"></span><span aria-label="Social profile"></span><span aria-label="Video channel"></span></div>
    <div class="toplinks">
      <a href="#"><svg width="16" height="11" viewBox="0 0 16 11"><rect x=".5" y=".5" width="15" height="10" fill="none" stroke="#fff"/><path d="M.5 .5 8 6l7.5-5.5" fill="none" stroke="#fff"/></svg>CONTACT</a>
      <a href="#"><svg width="12" height="13" viewBox="0 0 12 13"><path d="M5 1h6v11H5" fill="none" stroke="#fff" stroke-width="1.3"/><path d="M1 6.5h6M5 4l2.5 2.5L5 9" fill="none" stroke="#fff" stroke-width="1.3"/></svg>LOGIN</a>
    </div>
  </div>
  <div class="abs header"></div>
  <div class="abs logo-box"><i></i><b>TMRCL</b></div>
  <h1 class="abs site-title"><span>TEXAS MARSH REED</span><span>CONSERVATION LEAGUE.</span></h1>
  <div class="abs join">BECOME A MEMBER</div>
  <nav class="abs nav">
    <ul>
      <li class="active" style="left:90px">HOME</li>
      <li style="left:204px">ABOUT</li>
      <li style="left:308px">MEMBERS</li>
      <li style="left:432px">RESOURCES</li>
      <li style="left:569px">EVENTS</li>
      <li style="left:681px">MEMBERSHIP</li>
      <li style="left:825px">CONTACT</li>
    </ul>
  </nav>
</header>

<section class="abs slider">
  <div class="slide" role="img" aria-label="Photo of a calm pond covered in lily pads, with green trees on the far bank under a bright sky">
    <div class="arrow" style="left:0"><svg width="8" height="12" viewBox="0 0 8 12"><path d="M6 1 1.5 6 6 11" fill="none" stroke="#fff" stroke-width="2"/></svg></div>
    <div class="arrow" style="right:0"><svg width="8" height="12" viewBox="0 0 8 12"><path d="M2 1l4.5 5L2 11" fill="none" stroke="#fff" stroke-width="2"/></svg></div>
    <div class="caption">Promoting environmental stewardship through operations,research, education and outreach</div>
  </div>
</section>

<h2 class="abs welcome">Welcome to TMRCL</h2>
<p class="abs intro">The Texas Marsh Reed Conservation League, Inc. is an organization of scientists, educators, students, commercial pesticide applicators, administrators, and concerned individuals interested in the management and study of aquatic plants. The membership reflects a diversity of federal, state, and local agencies; universities and colleges around the world; corporations; and small businesses.</p>

<aside class="abs newsletter">
  <h3>Newsletter Signup</h3>
  <div class="field">Email Address</div>
  <div class="btn">Sign Up</div>
</aside>

<h2 class="abs events-title">Upcoming Events</h2>
<article class="abs event" style="top:795px">
  <div class="thumb" role="img" aria-label="Photo of a lily pond with trees under a blue sky" style="background:linear-gradient(180deg,#9cc2e6 0%,#cfe0ee 35%,#4f7a34 50%,#5d6e58 70%,#7a6a3a 100%)"></div>
  <div class="body">
    <h4>2014 Northeast Wetland Reed Society Annual Conference</h4>
    <time>January 21, 2014 -January 23, 2014</time>
    <p>Lorem Ipsum is simply dummy text of the printing and typesetting industry. Lorem Ipsum has been the industry's standard dummy text ever since the 1500s,</p>
  </div>
</article>
<div class="abs divider"></div>
<article class="abs event" style="top:922px">
  <div class="thumb" role="img" aria-label="Photo of tall reeds beside still water reflecting trees" style="background:linear-gradient(180deg,#e6eef0 0%,#6f9a45 35%,#3f6a2a 60%,#8aa6a0 80%,#4a6a30 100%)"></div>
  <div class="body">
    <h4>2014 Northeast Wetland Reed Society Annual Conference</h4>
    <time>January 21, 2014 -January 23, 2014</time>
    <p>Lorem Ipsum is simply dummy text of the printing and typesetting industry. Lorem Ipsum has been the industry's standard dummy text ever since the 1500s,</p>
  </div>
</article>
<div class="abs viewall">Veiw All</div>

<div class="abs ad" role="img" aria-label="Member advertisement placeholder showing product packaging over an underwater backdrop"></div>

<footer class="abs footer">
  <div class="footnav">Home<span class="sep">|</span>About<span class="sep">|</span>Members<span class="sep">|</span>Resources<span class="sep">|</span>Events<span class="sep">|</span>Membership<span class="sep">|</span>Contact</div>
  <div class="copy">Copyright © 2014 TMRCL. All rights reserved.</div>
  <a class="advertise" href="#">advertise with us</a>
  <div class="social" aria-label="Social profile links"><span aria-label="Social profile"></span><span aria-label="Social profile"></span><span aria-label="Video channel"></span></div>
</footer>
</body>
</html>
```